Plumbing website that stands out

Seo optimized, mobile friendly, easily editable word press Plumbing website with google reviews widget. And widget of revolving photos of completed work. Contact page and services page, about page. Will provide, “About” content. And photos Need all other content written.
Services include:
Water heater replacement
Tankless water heater installation
Kitchen and bath remodel
Drain cleaning and clog removal
Leak repair
Faucet repair and replacement

I will be adding services and photos of recent completed projects as time goes on.

```html
<!DOCTYPE html>
<html lang="en">
<head>
<meta charset="utf-8">
<title>Clearbrook Plumbing</title>
<link href="https://fonts.googleapis.com/css2?family=Montserrat:wght@400;500;600;700&family=Poppins:wght@400;500;600&display=swap" rel="stylesheet">
<style>
:root{
  --blue:#2a5ea8;
  --blue-dark:#1f4f8f;
  --navy:#173e75;
  --teal:#5bb8c9;
  --mint:#e2f1f3;
  --card:#eef1f5;
  --grey:#f3f4f5;
  --ink:#1c1c1c;
  --muted:#4a4a4a;
  --link:#4fa3cf;
  --white:#ffffff;
  --star:#f5a623;
}
*{box-sizing:border-box;margin:0;padding:0}
html,body{width:1200px;height:4413px;overflow:hidden}
body{position:relative;background:var(--white);font-family:"Poppins",Arial,sans-serif;color:var(--ink)}
.section{position:absolute;left:0;width:1200px}
.abs{position:absolute}
h2.title{font-family:"Montserrat",Arial,sans-serif;font-weight:700;font-size:20px;text-align:center;letter-spacing:.3px}

/* header */
.header{top:0;height:111px;background:var(--white)}
.brand{left:88px;top:26px;display:flex;flex-direction:column;align-items:center;gap:6px}
.brand .mark{width:26px;height:26px;background:var(--blue)}
.brand .name{font-family:"Montserrat",sans-serif;font-weight:600;font-size:17px;letter-spacing:3px;color:var(--navy)}
.nav{left:326px;top:43px;display:flex;gap:44px;font-family:"Montserrat",sans-serif;font-size:14px;font-weight:500}
.nav a{color:var(--ink);text-decoration:none}
.nav a.active{color:var(--blue);border-bottom:2px solid var(--blue);padding:0 0 10px}
.callout{left:803px;top:38px;font-size:9px}
.callout .phone{font-size:15px;font-weight:600;color:var(--blue);display:flex;align-items:center;gap:4px;margin-top:2px}
.btn-online{left:958px;top:35px;width:182px;height:42px;border-radius:21px;background:var(--blue);color:#fff;font-size:14px;font-weight:500;display:flex;align-items:center;justify-content:center;gap:8px}

/* hero */
.hero{top:111px;height:499px;background:linear-gradient(100deg,#4f79b8,#7d9fd0 55%,#a8bfe0)}
.hero h1{position:absolute;left:0;width:1200px;top:150px;text-align:center;font-family:"Montserrat",sans-serif;font-weight:600;font-size:41px;line-height:48px;color:#fff}
.hero p{position:absolute;left:400px;width:400px;top:268px;text-align:center;color:#fff;font-size:12px;line-height:22px}
.hero .cta{left:511px;top:346px;width:192px;height:48px;border-radius:6px;background:#fff;color:var(--blue);font-size:13px;font-weight:600;display:flex;align-items:center;justify-content:center}
.arrow{width:55px;height:54px;background:#fff;display:flex;align-items:center;justify-content:center}

/* services */
.services{top:610px;height:791px}
.services h2{position:absolute;top:62px;left:0;width:1200px;line-height:25px}
.services .lead{position:absolute;top:131px;left:330px;width:540px;text-align:center;font-size:12px;line-height:22px}
.svc{position:absolute;width:298px;height:233px;background:var(--card);border-top:5px solid var(--blue);text-align:center;padding:28px 34px 0}
.svc.featured{background:var(--mint);box-shadow:0 4px 8px rgba(0,0,0,.15)}
.svc svg{display:block;margin:0 auto 12px}
.svc h3{font-family:"Montserrat",sans-serif;font-weight:600;font-size:15px;line-height:18px;margin-bottom:12px}
.svc p{font-size:10px;line-height:13px;color:var(--muted)}

/* about */
.about{top:1401px;height:500px;background:var(--grey)}
.about h2{position:absolute;left:144px;top:107px;font-family:"Montserrat",sans-serif;font-size:19px;font-weight:700}
.about p{position:absolute;left:144px;top:150px;width:410px;font-size:13px;line-height:22.5px}
.about .btn{left:144px;top:319px;width:160px;height:46px;border-radius:6px;background:var(--blue);color:#fff;font-size:12px;display:flex;align-items:center;justify-content:center}
.about .photo{left:623px;top:0;width:577px;height:500px;background:linear-gradient(160deg,#e9ecef,#c9d3df 60%,#9fb1c9)}

/* why */
.why{top:1901px;height:369px;background:var(--mint)}
.why h2{position:absolute;top:65px;left:0;width:1200px}
.why .col{position:absolute;top:105px;width:247px;height:210px;text-align:center;padding-top:40px}
.why .col.line{border-right:1px solid #a9c3c8}
.why .ico{width:62px;height:62px;background:var(--teal);margin:0 auto 22px;display:flex;align-items:center;justify-content:center}
.why h3{font-family:"Montserrat",sans-serif;font-size:12px;font-weight:600;margin-bottom:8px}
.why p{font-size:9.5px;line-height:12px;width:170px;margin:0 auto;color:var(--muted)}

/* projects */
.projects{top:2270px;height:672px;background:var(--blue)}
.projects h2{position:absolute;top:56px;left:0;width:1200px;color:#fff}
.tabs{left:264px;top:111px;display:flex;gap:12px}
.tabs span{width:102px;height:37px;border:1px solid #5d86c0;color:#9db9e0;font-size:12px;display:flex;align-items:center;justify-content:center}
.tabs span.on{background:var(--teal);border-color:var(--teal);color:#fff}
.tile{position:absolute;width:223px;height:205px;background:linear-gradient(150deg,#c8d6e6,#7f9ec4)}
.tile.hl{background:linear-gradient(150deg,#9fd4da,#6bbcc7);color:#fff;font-size:12px;display:flex;align-items:center;justify-content:center}

/* testimonials */
.reviews{top:2942px;height:443px;background:linear-gradient(180deg,#eef1f4,#e3e8ee)}
.reviews h2{position:absolute;top:68px;left:0;width:1200px}
.review{position:absolute;top:126px;width:320px;height:199px;background:#fff;padding:32px 28px 0}
.review h3{font-family:"Poppins",sans-serif;font-weight:500;font-size:19px;text-align:center;margin-bottom:10px}
.stars{display:flex;gap:3px;margin-bottom:14px}
.review p{font-size:12px;line-height:15px}

/* news */
.news{top:3385px;height:502px}
.news h2{position:absolute;top:76px;left:0;width:1200px}
.post{position:absolute;top:119px;width:306px;height:311px;background:var(--card);padding:16px 14px 0}
.post .img{width:278px;height:148px;background:linear-gradient(150deg,#dfe5ec,#9fb0c5)}
.post h3{font-family:"Montserrat",sans-serif;font-size:14px;font-weight:600;line-height:20px;margin:18px 12px 8px}
.post p{font-size:9.5px;line-height:17px;margin:0 12px 10px;color:var(--muted)}
.post a{font-size:11px;color:var(--link);margin-left:12px;text-decoration:none}

/* cta band */
.band{top:3887px;height:223px;background:linear-gradient(90deg,#4a77b4,#6e97ca)}
.band h2{position:absolute;left:223px;top:89px;font-family:"Montserrat",sans-serif;font-weight:500;font-size:29px;color:#fff}
.band .btn{left:716px;top:79px;width:260px;height:62px;border-radius:31px;background:#fff;color:var(--blue);font-size:14px;font-weight:600;display:flex;align-items:center;justify-content:center}

/* footer */
.footer{top:4110px;height:303px;background:var(--navy);color:#fff}
.footer .brand{left:90px;top:40px}
.footer .brand .mark{width:34px;height:34px;background:#fff}
.footer .brand .name{color:#fff;font-size:22px}
.footer h4{font-family:"Montserrat",sans-serif;font-size:13px;font-weight:600;margin-bottom:18px}
.footer ul{list-style:none;font-size:12px;line-height:27px}
.social{display:flex;gap:14px}
.social span{width:20px;height:20px;border-radius:50%;background:#fff}
.copy{left:0;width:1200px;top:273px;text-align:center;font-size:11px}
</style>
</head>
<body>

<header class="section header">
  <div class="abs brand"><span class="mark"></span><span class="name">CLEARBROOK</span></div>
  <nav class="abs nav">
    <a class="active" href="#">Home</a><a href="#">About Us</a><a href="#">Services &#8964;</a><a href="#">Contact Us</a>
  </nav>
  <div class="abs callout">Need Help Now? Call Us!
    <div class="phone"><svg width="14" height="14" viewBox="0 0 24 24"><path d="M6 3l3 4-2 2c1 3 4 6 7 7l2-2 4 3-2 3C10 20 4 14 3 5z" fill="none" stroke="#2a5ea8" stroke-width="2"/></svg>(555) 013 2468</div>
  </div>
  <div class="abs btn-online">Schedule Online
    <svg width="16" height="16" viewBox="0 0 24 24"><rect x="3" y="5" width="18" height="16" rx="2" fill="none" stroke="#fff" stroke-width="2"/><path d="M8 13l3 3 5-6" fill="none" stroke="#fff" stroke-width="2"/></svg></div>
</header>

<section class="section hero" role="img" aria-label="Plumber in blue uniform working under a sink">
  <div class="abs arrow" style="left:78px;top:217px"><svg width="12" height="16"><path d="M9 2L3 8l6 6" fill="none" stroke="#222" stroke-width="2"/></svg></div>
  <div class="abs arrow" style="left:1045px;top:227px"><svg width="12" height="16"><path d="M3 2l6 6-6 6" fill="none" stroke="#222" stroke-width="2"/></svg></div>
  <h1>Fast &amp; Efficient Plumbing<br>Services</h1>
  <p>Lorem ipsum dolor sit amet consectetur. In nunc non scelerisque rhoncus. Ac fusce ipsum pharetra eu.</p>
  <div class="abs cta">Get Free Estimate</div>
</section>

<section class="section services">
  <h2 class="title">WE PROVIDE RESIDENTIAL &amp; COMMERCIAL<br>PLUMBING SERVICES</h2>
  <p class="lead">Clearbrook is a Professional Plumbing Contractor that provide Residential and Commercial Plumbing Services. Rely on our Experienced and Courteous team for dependable and Comprehensive plumbing repair and service. Contact us or Request a Quote</p>

  <div class="svc featured" style="left:144px;top:236px">
    <svg width="34" height="48" viewBox="0 0 34 48"><rect x="4" y="2" width="26" height="40" rx="3" fill="none" stroke="#2a5ea8" stroke-width="3"/><circle cx="17" cy="16" r="6" fill="none" stroke="#2a5ea8" stroke-width="3"/><path d="M10 46h14" stroke="#2a5ea8" stroke-width="3"/></svg>
    <h3>Water Heater Replacement</h3>
    <p>We Install, Repair and Manage all types of Hot Water Heaters including Thankless water Heaters and others</p>
  </div>
  <div class="svc" style="left:451px;top:236px">
    <svg width="36" height="44" viewBox="0 0 36 44"><rect x="3" y="2" width="30" height="40" rx="3" fill="none" stroke="#2a5ea8" stroke-width="3"/><path d="M3 12h30M3 22h30M3 32h30" stroke="#2a5ea8" stroke-width="3"/></svg>
    <h3>Tankless Water Heater Installation</h3>
    <p>Lorem ipsum dolor sit amet consectetur. Facilisis nulla leo pulvinar quam suspendisse nec id turpis ac. Ullamcorper ac eu ullamcorper in. Purus nibh vel sed.</p>
  </div>
  <div class="svc" style="left:762px;top:236px">
    <svg width="52" height="36" viewBox="0 0 52 36"><rect x="2" y="6" width="48" height="28" fill="none" stroke="#2a5ea8" stroke-width="3"/><path d="M2 16h48M18 16v18M34 16v18M20 6V2h12v4" stroke="#2a5ea8" stroke-width="3" fill="none"/></svg>
    <h3>Kitchen and Bath Remodel</h3>
    <p>Lorem ipsum dolor sit amet consectetur. Facilisis nulla leo pulvinar quam suspendisse nec id turpis ac. Ullamcorper ac eu ullamcorper in. Purus nibh vel sed.</p>
  </div>
  <div class="svc" style="left:144px;top:496px">
    <svg width="44" height="44" viewBox="0 0 44 44"><path d="M30 4l10 10-16 16-10-10z" fill="#2a5ea8"/><path d="M14 20L4 40" stroke="#2a5ea8" stroke-width="4"/></svg>
    <h3>Drain Cleaning and Log Removal</h3>
    <p>We Install, Repair and Manage all types of Hot Water Heaters including Thankless water Heaters and others</p>
  </div>
  <div class="svc" style="left:451px;top:496px">
    <svg width="44" height="44" viewBox="0 0 44 44"><path d="M2 4h40v16H2z" fill="none" stroke="#2a5ea8" stroke-width="3"/><path d="M22 26c-3 5-3 8 0 8s3-3 0-8zM30 36l2 4" stroke="#2a5ea8" stroke-width="3" fill="#2a5ea8"/></svg>
    <h3>Leak Repair</h3>
    <p>Lorem ipsum dolor sit amet consectetur. Facilisis nulla leo pulvinar quam suspendisse nec id turpis ac. Ullamcorper ac eu ullamcorper in. Purus nibh vel sed.</p>
  </div>
  <div class="svc" style="left:762px;top:496px">
    <svg width="36" height="44" viewBox="0 0 36 44"><path d="M8 42V16a10 10 0 0 1 20 0v6" fill="none" stroke="#2a5ea8" stroke-width="3"/><path d="M28 28v4M28 36v2" stroke="#2a5ea8" stroke-width="3"/></svg>
    <h3>Tankless Water Heater Installation</h3>
    <p>Lorem ipsum dolor sit amet consectetur. Facilisis nulla leo pulvinar quam suspendisse nec id turpis ac. Ullamcorper ac eu ullamcorper in. Purus nibh vel sed.</p>
  </div>
</section>

<section class="section about">
  <h2>ABOUT US</h2>
  <p>Lorem ipsum dolor sit amet consectetur. In nunc non scelerisque rhoncus. Ac fusce ipsum pharetra eu. Enim et augue urna turpis. Turpis libero at facilisi vulputate lobortis lectus dignissim. Faucibus dictumst in diam donec. Malesuada dolor ullamcorper lorem potenti sem leo. Elementum eu leo praesent sed. Non tincidunt purus massa eget scelerisque. Porta nullam ultrices eget metus nunc mauris leo sed.</p>
  <div class="abs btn">Learn More</div>
  <div class="abs photo" role="img" aria-label="Smiling plumber in overalls holding a wrench in a kitchen"></div>
</section>

<section class="section why">
  <h2 class="title">WHY CHOOSE US ?</h2>
  <div class="col line" style="left:112px">
    <div class="ico"><svg width="34" height="34" viewBox="0 0 34 34"><circle cx="17" cy="17" r="13" fill="none" stroke="#fff" stroke-width="2.5"/><path d="M17 9v8l6 4" stroke="#fff" stroke-width="2.5" fill="none"/></svg></div>
    <h3>24 HOURS SUPPORT</h3><p>We Provide 24 Hours Support to our Clients for Emergency Plumbing Services.</p>
  </div>
  <div class="col line" style="left:359px">
    <div class="ico"><svg width="34" height="34" viewBox="0 0 34 34"><circle cx="17" cy="14" r="9" fill="none" stroke="#fff" stroke-width="2.5"/><path d="M11 21l-3 10 9-4 9 4-3-10" fill="none" stroke="#fff" stroke-width="2.5"/></svg></div>
    <h3>LINCESED AND INSURED</h3><p>All of our Plumbing Team Members are fully licensed, bonded and insured.</p>
  </div>
  <div class="col line" style="left:606px">
    <div class="ico"><svg width="36" height="34" viewBox="0 0 36 34"><circle cx="18" cy="14" r="6" fill="#fff"/><path d="M6 32c0-8 6-11 12-11s12 3 12 11z" fill="#fff"/><circle cx="6" cy="6" r="3" fill="#fff"/><circle cx="18" cy="3" r="2.5" fill="#fff"/><circle cx="30" cy="6" r="3" fill="#fff"/></svg></div>
    <h3>REPUTABLE COMPANY</h3><p>Operating for more than 25 years, earning a reputation for service and beautiful work.</p>
  </div>
  <div class="col" style="left:853px">
    <div class="ico"><svg width="36" height="34" viewBox="0 0 36 34"><path d="M4 6h28v18H14l-8 7v-7H4z" fill="#fff"/><circle cx="12" cy="15" r="2" fill="#5bb8c9"/><circle cx="18" cy="15" r="2" fill="#5bb8c9"/><circle cx="24" cy="15" r="2" fill="#5bb8c9"/></svg></div>
    <h3>FREE QUOTE &amp; ESTIMATE</h3><p>We Provide 24 Hours Support to our Clients for Emergency Plumbing Services.</p>
  </div>
</section>

<section class="section projects">
  <h2 class="title">OUR RECENT PROJECTS</h2>
  <div class="abs tabs"><span class="on">All</span><span>Bathroom</span><span>Heaters</span><span>Installation</span><span>Kitchen</span><span>Waters</span></div>
  <div class="tile" style="left:141px;top:186px" role="img" aria-label="Hand tightening a chrome sink pipe with a wrench"></div>
  <div class="tile" style="left:373px;top:186px" role="img" aria-label="Plumber cutting a pipe"></div>
  <div class="tile hl" style="left:605px;top:186px" role="img" aria-label="Tankless water filtration project">Tankless Water Filtration</div>
  <div class="tile" style="left:836px;top:186px" role="img" aria-label="Plumber repairing pipes under a kitchen sink"></div>
  <div class="tile" style="left:141px;top:405px" role="img" aria-label="Wrench on a kitchen faucet"></div>
  <div class="tile" style="left:373px;top:405px" role="img" aria-label="Plumber with tools kneeling by a pipe"></div>
  <div class="tile" style="left:605px;top:405px" role="img" aria-label="Plumber fixing overhead pipes"></div>
  <div class="tile" style="left:836px;top:405px" role="img" aria-label="Industrial pipe installation"></div>
</section>

<section class="section reviews" role="img" aria-label="Softly faded bathroom interior background">
  <h2 class="title">CLIENT TESTIMONIALS</h2>
  <div class="review" style="left:105px">
    <h3>Dana Whitfield</h3>
    <div class="stars"><svg width="150" height="26" viewBox="0 0 150 26"><g fill="#f5a623"><path id="st" d="M13 1l3.5 8 8.5.7-6.5 5.6 2 8.4L13 19l-7.5 4.7 2-8.4L1 9.7 9.5 9z"/><use href="#st" x="30"/><use href="#st" x="60"/><use href="#st" x="90"/><use href="#st" x="120"/></g></svg></div>
    <p>The technician was polite and took care of a simple water heater problem and Took the time to explain things to me. I am very pleased</p>
  </div>
  <div class="review" style="left:445px">
    <h3>Marcus Ellory</h3>
    <div class="stars"><svg width="150" height="26" viewBox="0 0 150 26"><g fill="#f5a623"><use href="#st"/><use href="#st" x="30"/><use href="#st" x="60"/><use href="#st" x="90"/><use href="#st" x="120"/></g></svg></div>
    <p>The technician was polite and took care of a simple water heater problem and Took the time to explain things to me. I am very pleased</p>
  </div>
  <div class="review" style="left:778px">
    <h3>Dana Whitfield</h3>
    <div class="stars"><svg width="150" height="26" viewBox="0 0 150 26"><g fill="#f5a623"><use href="#st"/><use href="#st" x="30"/><use href="#st" x="60"/><use href="#st" x="90"/><use href="#st" x="120"/></g></svg></div>
    <p>The technician was polite and took care of a simple water heater problem and Took the time to explain things to me. I am very pleased</p>
  </div>
</section>

<section class="section news">
  <h2 class="title">LATEST NEWS</h2>
  <article class="post" style="left:117px">
    <div class="img" role="img" aria-label="Plumber holding tools and hoses"></div>
    <h3>Lorem ipsum dolor sit amet consectetur</h3>
    <p>Lorem ipsum dolor sit amet consectetur. In nunc non scelerisque rhoncus. Ac fusce ipsum pharetra eu.</p>
    <a href="#">Read More</a>
  </article>
  <article class="post" style="left:446px">
    <div class="img" role="img" aria-label="Wrench on a pipe under a sink"></div>
    <h3>Lorem ipsum dolor sit amet consectetur</h3>
    <p>Lorem ipsum dolor sit amet consectetur. In nunc non scelerisque rhoncus. Ac fusce ipsum pharetra eu.</p>
    <a href="#">Read More</a>
  </article>
  <article class="post" style="left:776px">
    <div class="img" role="img" aria-label="Plumber working beneath a kitchen sink"></div>
    <h3>Lorem ipsum dolor sit amet consectetur</h3>
    <p>Lorem ipsum dolor sit amet consectetur. In nunc non scelerisque rhoncus. Ac fusce ipsum pharetra eu.</p>
    <a href="#">Read More</a>
  </article>
</section>

<section class="section band" role="img" aria-label="Bathroom sink in blue tint">
  <h2>HAVE A PLUMBING PROBLEM?</h2>
  <div class="abs btn">GET FREE ESTIMATE NOW</div>
</section>

<footer class="section footer">
  <div class="abs brand"><span class="mark"></span><span class="name">CLEARBROOK</span></div>
  <div class="abs" style="left:382px;top:42px"><h4>QUICKLINKS</h4><ul><li>Home</li><li>About Us</li><li>Our Services</li><li>Contact Us</li></ul></div>
  <div class="abs" style="left:579px;top:42px"><h4>SERVICES</h4><ul><li>Water heater replacement</li><li>Tankless water heater installation</li><li>Kitchen and bath remodel</li><li>Drain cleaning and clog removal</li><li>Leak repair/Faucet repair and replacement</li></ul></div>
  <div class="abs" style="left:868px;top:40px"><h4>CONNECTED WITH US</h4><div class="social"><span></span><span></span><span></span><span></span><span></span></div></div>
  <div class="abs copy">©2022 CLEARBROOK PLUMBING. All rights reserved.</div>
</footer>

</body>
</html>
```